Financial Planner Letterhead + Business Card

We need letterhead and business card designed for a financial advisory firm. The letterhead and business card should make use of our existing logo, and colors should be similar to logo...which is attached. we want to communicate safety, trust, stability. We need the ability to edit the final files so that we can add additional phone number

Both the letterhead and business card MUST contain the following disclosure: Most of the samples so far did not follow this instruction.

Securities and advisory services offered through Harborview Capital Alliance®, member BXQMA/TOLV, a Registered Investment Adviser. Fixed insurance products and services offered through DRW Insurance Agency

details
Tessa Marlow
President & Wealth Advisor
812 E. 9th Street, Suite 6
Brierly, TX 75391
555-512-0948
Tessa@lumenrw.example
web: www.lumenridgewealth.example

Target Market(s)

all adults - primary those 50 and older, generally college degreed professionals

Industry/Entity Type

Business

Contact Information for Business Card

must include this disclosure:
Securities and advisory services offered through Harborview Capital Alliance®, member BXQMA/TOLV, a Registered Investment Adviser

details
Tessa Marlow
Brierly, TX 75391
555-512-0948
Tessa@lumenrw.example

Font styles to use
Sans Serif

Colors

Designer to choose colors to be used in the design.

Requirements
Must have
• logo, name/address info
• appealing visually, stands out without being overwhelming
• MUST HAVE DISCLOSURE !! (in footer of letterhead & on back of business card).
• Securities and advisory services offered through Harborview Capital Alliance®, member BXQMA/TOLV, a Registered Investment Adviser. Fixed insurance products and services offered through DRW Insurance Agency
Should not have
• lines indicating upward movement (such as up arrows)

```html
<!DOCTYPE html>
<html lang="en">
<head>
<meta charset="utf-8">
<title>Lumen Ridge Wealth – Letterhead</title>
<link rel="stylesheet" href="https://fonts.googleapis.com/css2?family=Open+Sans:wght@400;600;700&display=swap">
<style>
  :root{
    --backdrop:#8a8178;
    --paper:#ffffff;
    --navy:#1f2d6b;
    --sky:#1e9ad6;
    --green:#8cc63f;
    --ink:#3b3b3b;
    --watermark:#f0f0f0;
  }
  *{box-sizing:border-box;margin:0;padding:0}
  html,body{width:1200px;height:795px;overflow:hidden}
  body{background:var(--backdrop);font-family:"Open Sans",Arial,sans-serif;color:var(--ink)}
  .letterhead{
    position:absolute;left:331px;top:18px;width:538px;height:760px;
    background:var(--paper);box-shadow:0 6px 18px rgba(0,0,0,.25);
  }
  .brand{position:absolute;left:44px;top:40px;display:flex;align-items:center;gap:8px}
  .brand-mark{width:18px;height:18px;background:var(--green)}
  .brand-name{font-weight:700;font-size:20px;color:var(--navy);letter-spacing:.2px}
  .watermark{position:absolute;left:120px;top:175px;width:300px;height:300px;background:var(--watermark)}
  .contact{position:absolute;right:34px;top:612px;text-align:right;font-size:8px;line-height:14px;color:var(--ink)}
  .contact li{list-style:none;display:flex;justify-content:flex-end;align-items:center;gap:5px}
  .contact svg{width:9px;height:9px}
  .rule{position:absolute;left:34px;right:34px;top:660px;height:1px;background:var(--green)}
  .address{position:absolute;left:34px;top:672px;font-size:8px;line-height:12px;font-style:normal}
  .address .firm{font-weight:700;color:var(--navy)}
  .address .firm span{color:var(--green)}
  .disclosure{
    position:absolute;left:200px;right:0;top:668px;height:52px;
    background:linear-gradient(90deg,var(--sky),var(--navy));
    color:#fff;font-size:7.5px;line-height:11px;padding:8px 16px;
  }
</style>
</head>
<body>
  <main class="letterhead">
    <header class="brand">
      <span class="brand-mark"></span>
      <span class="brand-name">Lumen Ridge Wealth</span>
    </header>

    <div class="watermark" role="img" aria-label="Faint brand watermark"></div>

    <ul class="contact">
      <li>555-512-0948 <svg viewBox="0 0 10 10"><circle cx="5" cy="5" r="5" fill="#1f2d6b"/></svg></li>
      <li>Tessa@lumenrw.example <svg viewBox="0 0 10 10"><circle cx="5" cy="5" r="5" fill="#1f2d6b"/></svg></li>
      <li>www.lumenridgewealth.example <svg viewBox="0 0 10 10"><circle cx="5" cy="5" r="5" fill="#1f2d6b"/></svg></li>
    </ul>

    <div class="rule"></div>

    <address class="address">
      <div class="firm">Lumen Ridge <span>Wealth</span></div>
      <div>812 E. 9th Street, Suite 6</div>
      <div>Brierly, TX 75391</div>
    </address>

    <footer class="disclosure">
      Securities and advisory services offered through Harborview Capital Alliance®, member BXQMA/TOLV, a Registered Investment Adviser. Fixed insurance products and services offered through DRW Insurance Agency
    </footer>
  </main>
</body>
</html>
```